West Australian based aspiring best selling novelist needs a book cover design

I have a completed manuscript for a fiction novel about 3 women whose partners work away in fly in fly out (FIFO) jobs. One woman has three young kids (boy, 8, boy 6 and girl 18months old), one woman is the first woman's sister and is young and beautiful but a bit troubled and one woman works on reception at a strip club. All three want to be independent but still miss their lovers. Location is the Midwest of Western Australia where there are beautiful beaches, blue skies and crayfish. The title is 'Seven Kites Over the Salt Flats.' Author's name is Ruth Dalby. I need a book cover design. I am unsure whether to try and capture the spirit of those women or the landscape or do a simple graphic design like crosses on a dateless calendar, counting down the days (Two weeks crossed off then one happy week when the lover is home and then another two sad weeks). The final design should lure people in to want to read the text. Thank you

Target Market(s)
Women, particularly those who are struggling with being a stay at home lover.

Must Have:
- Soul, an understanding of the complexity of loneliness. The women are strong and interesting- not flaky. This is NOT a romance novel. It is a quirky story with heart.

Nice to Have:
- A design that is striking but not too busy

Should Not Have:
- No trashy images of women. Should NOT look like a romance novel.

Target Market(s)

Women 18 upwards

Industry/Entity Type

Book Publisher

Font styles to use
Other font styles liked:
• unsure

Requirements
Must have
• A bit of quirkiness, soul, loneliness, independence
Nice to have
• Something striking but not too busy. I trust your skills!
Should not have
• Not look like a romance novel. The genre is more contemporary chick literature

```html
<!DOCTYPE html>
<html lang="en">
<head>
<meta charset="utf-8">
<title>Seven Kites Over the Salt Flats – Cover Options</title>
<link rel="stylesheet" href="https://fonts.googleapis.com/css2?family=Noto+Serif:ital,wght@0,700;1,700&family=Josefin+Sans:wght@600;700&display=swap">
<style>
  :root {
    --backdrop: #f1f1f1;
    --sky-top: #86b6de;
    --sky-mid: #c4ddf1;
    --sky-pale: #eef2f8;
    --sky-low: #a3b2da;
    --cloud: #ffffff;
    --title-red: #b8202a;
    --ring-red: #e2372c;
    --subtitle-blue: #4f66a6;
    --author-white: #ffffff;
    --hair: #d6b07c;
    --skin: #b7694b;
    --top-olive: #8d8b68;
    --plane-grey: #8d9bab;
    --plane-light: #b4c0cc;
    --calendar: rgba(255,255,255,0.6);
  }
  * { margin: 0; padding: 0; box-sizing: border-box; }
  html, body {
    width: 1200px; height: 930px; overflow: hidden;
    background: var(--backdrop);
  }
  .stage { position: relative; width: 1200px; height: 930px; }

  .cover {
    position: absolute; top: 142px;
    width: 448px; height: 664px; overflow: hidden;
    box-shadow: 0 6px 18px rgba(0,0,0,0.18);
  }
  .cover--serif { left: 86px; }
  .cover--sans  { left: 650px; }

  .cover__sky {
    position: absolute; inset: 0;
    background:
      radial-gradient(ellipse 40% 14% at 58% 4%, var(--cloud) 70%, transparent 72%),
      radial-gradient(ellipse 30% 12% at 92% 14%, var(--cloud) 70%, transparent 72%),
      radial-gradient(ellipse 26% 8% at 12% 30%, rgba(255,255,255,0.9) 70%, transparent 72%),
      linear-gradient(180deg, var(--sky-top) 0%, var(--sky-mid) 38%, var(--sky-pale) 55%, var(--sky-pale) 78%, var(--sky-low) 100%);
  }
  .cover__calendar {
    position: absolute; left: 240px; top: 380px; width: 208px; height: 210px;
    background: var(--calendar);
    border-radius: 4px;
  }
  .cover__figure {
    position: absolute; left: 8px; top: 266px; width: 258px; height: 398px;
    border-radius: 110px 110px 24px 24px;
    background: linear-gradient(180deg, var(--hair) 0%, var(--hair) 40%, var(--skin) 46%, var(--skin) 58%, var(--top-olive) 64%, var(--top-olive) 100%);
  }
  .cover__plane {
    position: absolute; left: 318px; top: 112px; width: 126px; height: 30px;
    border-radius: 15px;
    background: linear-gradient(180deg, var(--plane-light), var(--plane-grey));
    transform: rotate(-52deg);
  }

  .cover__ring { position: absolute; left: 0; top: 0; width: 448px; height: 664px; }

  .cover__lead {
    position: absolute; left: 16px; top: 30px;
    color: var(--author-white);
    text-shadow: 0 1px 3px rgba(60,80,120,0.35);
    line-height: 1;
  }
  .cover--serif .cover__lead {
    font-family: "Noto Serif", Georgia, serif; font-style: italic; font-weight: 700; font-size: 40px;
  }
  .cover--sans .cover__lead {
    font-family: "Josefin Sans", Arial, sans-serif; font-weight: 700; font-size: 33px; letter-spacing: 2px; top: 38px;
  }

  .cover__title {
    position: absolute; left: 6px; width: 448px; top: 104px;
    text-align: center;
    font-family: "Josefin Sans", Arial, sans-serif; font-weight: 700;
    font-size: 66px; line-height: 70px;
    color: var(--title-red); opacity: 0.94;
  }
  .cover__title span { display: block; }

  .cover__subtitle {
    position: absolute; right: 12px; top: 282px;
    text-align: right; color: var(--subtitle-blue); line-height: 1.1;
  }
  .cover--serif .cover__subtitle {
    font-family: "Noto Serif", Georgia, serif; font-style: italic; font-weight: 700; font-size: 40px;
  }
  .cover--sans .cover__subtitle {
    font-family: "Josefin Sans", Arial, sans-serif; font-weight: 700; font-size: 38px; letter-spacing: 1px; top: 288px;
  }

  .cover__author {
    position: absolute; left: 0; width: 448px; bottom: 24px;
    text-align: center;
    font-family: "Noto Serif", Georgia, serif; font-weight: 700; font-size: 38px;
    color: var(--author-white);
    text-shadow: 0 1px 4px rgba(40,40,60,0.45);
  }
</style>
</head>
<body>
<main class="stage">

  <article class="cover cover--serif">
    <div class="cover__sky" role="img" aria-label="Bright blue sky with white clouds"></div>
    <div class="cover__calendar" role="img" aria-label="Faded calendar page with dates"></div>
    <div class="cover__figure" role="img" aria-label="Woman with braided blonde hair in an olive tank top, seen from behind"></div>
    <div class="cover__plane" role="img" aria-label="Passenger plane flying upward"></div>
    <p class="cover__lead">Seven</p>
    <h1 class="cover__title"><span>KITES</span><span>OVER THE</span></h1>
    <svg class="cover__ring" viewBox="0 0 448 664" aria-hidden="true">
      <ellipse cx="240" cy="180" rx="188" ry="98" fill="none" stroke="var(--ring-red)" stroke-width="5" transform="rotate(-5 240 180)"/>
      <path d="M210 88 Q320 78 410 104" fill="none" stroke="var(--ring-red)" stroke-width="3"/>
    </svg>
    <p class="cover__subtitle">Salt Flats</p>
    <p class="cover__author">Ruth Dalby</p>
  </article>

  <article class="cover cover--sans">
    <div class="cover__sky" role="img" aria-label="Bright blue sky with white clouds"></div>
    <div class="cover__calendar" role="img" aria-label="Faded calendar page with dates"></div>
    <div class="cover__figure" role="img" aria-label="Woman with braided blonde hair in an olive tank top, seen from behind"></div>
    <div class="cover__plane" role="img" aria-label="Passenger plane flying upward"></div>
    <p class="cover__lead">SEVEN</p>
    <h1 class="cover__title"><span>KITES</span><span>OVER THE</span></h1>
    <svg class="cover__ring" viewBox="0 0 448 664" aria-hidden="true">
      <ellipse cx="240" cy="180" rx="188" ry="98" fill="none" stroke="var(--ring-red)" stroke-width="5" transform="rotate(-5 240 180)"/>
      <path d="M210 88 Q320 78 410 104" fill="none" stroke="var(--ring-red)" stroke-width="3"/>
    </svg>
    <p class="cover__subtitle">SALT FLATS</p>
    <p class="cover__author">Ruth Dalby</p>
  </article>

</main>
</body>
</html>
```